r-brightlayer needs new website

need to get completely new updated site for r-brightlayer.com
general business concepts can be started from that site and I can offer specifick input about business operations and goals. would like to offer on-line ordering, service requests, and payments if possible.

```html
<!DOCTYPE html>
<html lang="en">
<head>
<meta charset="utf-8">
<title>R-Brightlayer</title>
<link href="https://fonts.googleapis.com/css2?family=Lato:wght@400;700&display=swap" rel="stylesheet">
<style>
:root{
  --orange:#e8800d;
  --ink:#1d1d1d;
  --text:#333;
  --muted:#888;
  --line:#e2e2e2;
  --panel:#f4f4f4;
  --footer:#000;
  --field:#1f1f1f;
}
*{box-sizing:border-box;margin:0;padding:0}
html,body{width:677px;height:1200px;overflow:hidden;background:#fff}
body{position:relative;font-family:'Lato',sans-serif;color:var(--text)}
.abs{position:absolute}
/* header */
.brand{left:45px;top:20px;display:flex;align-items:center;gap:6px;font-size:15px;font-weight:700;color:var(--ink);letter-spacing:.5px}
.brand-dot{width:14px;height:14px;border-radius:50%;background:var(--orange)}
.contact-top{top:24px;font-size:8.5px;display:flex;align-items:center;gap:6px}
.contact-top.mail{left:425px;color:var(--orange)}
.contact-top.tel{left:564px;color:var(--ink);font-weight:700}
.nav{left:0;top:62px;width:677px;height:28px;border-top:1px solid var(--line);border-bottom:1px solid var(--line);background:#fafafa}
.nav-item{top:0;height:27px;line-height:27px;font-size:8.5px;color:var(--ink);text-align:center}
.nav-item.active{background:var(--orange);color:#fff}
.nav-sep{top:0;width:1px;height:27px;background:var(--line)}
.search{left:502px;top:6px;width:130px;height:16px;background:#ececec;font-size:8px;color:#aaa;padding:3px 8px}
.search-btn{right:3px;top:3px;width:10px;height:10px;background:#fff;border:1px solid var(--orange)}
/* hero */
.hero{left:0;top:90px;width:677px;height:308px;background:linear-gradient(110deg,#8d8781 0%,#b7aea6 35%,#d8a77f 65%,#e6b08c 85%,#c89a7c 100%)}
.hero-caption{left:45px;top:299px;width:199px;height:66px;background:rgba(40,40,40,.85);color:#fff;padding:12px 22px}
.hero-caption h2{font-size:20px;font-weight:400;line-height:1.1}
.hero-caption p{font-size:7.5px;line-height:1.3}
.dots{left:45px;top:366px;width:34px;height:15px;background:#222;display:flex;gap:3px;align-items:center;justify-content:center}
.dots i{width:3px;height:3px;background:#fff}
.dots i:first-child{background:var(--orange)}
.arrow{top:361px;width:20px;height:20px;background:var(--orange)}
/* sections */
.h-sec{font-size:17px;font-weight:400;color:var(--ink)}
.rule{height:2px;background:var(--orange)}
.para{font-size:8px;line-height:13.6px;color:var(--text)}
.btn{width:104px;height:21px;background:var(--orange);color:#fff;font-size:8.5px;text-align:center;line-height:21px}
.about-photo{left:408px;top:458px;width:224px;height:224px;border-radius:50%;background:radial-gradient(circle at 40% 40%,#e8cfc6,#b48e86 60%,#6f5a58)}
.solutions{left:0;top:728px;width:677px;height:268px;background:var(--panel)}
.sol-frame{left:342px;top:768px;width:292px;height:206px;background:#fff;border:1px solid #dde4ea}
.sol-photo{left:355px;top:779px;width:267px;height:182px;background:radial-gradient(circle at 55% 40%,#6fb6dd,#2c6f9c 60%,#164d74)}
/* footer */
.footer{left:0;top:996px;width:677px;height:172px;background:var(--footer);color:#fff}
.f-brand{left:44px;top:34px;font-size:14px;font-weight:700;display:flex;gap:6px;align-items:center}
.f-brand .brand-dot{width:12px;height:12px}
.f-about{left:46px;top:76px;width:110px;font-size:7.3px;line-height:9.5px;font-weight:700}
.f-more{left:44px;top:127px;font-size:7.5px;font-weight:700}
.f-head{top:45px;font-size:8px;font-weight:700}
.f-head:after{content:"";display:block;width:26px;height:2px;background:#fff;margin-top:4px}
.f-list{top:72px;list-style:none;font-size:7.5px;line-height:14.2px}
.f-list li:before{content:"\25AA";margin-right:6px;font-size:6px}
.f-contact{left:300px;top:72px;font-size:7.8px;line-height:14.4px;font-weight:700}
.f-contact td{vertical-align:top;padding:0}
.field{background:var(--field);border:1px solid #333;font-size:7px;color:#bbb;padding:3px 6px}
.send{left:477px;top:119px;width:155px;height:16px;background:var(--orange);font-size:7.5px;font-weight:700;text-align:center;line-height:16px}
.copy{left:46px;top:1176px;font-size:8px;color:var(--text)}
.social{top:1177px;width:10px;height:10px;border-radius:50%;background:#444}
</style>
</head>
<body>

<header>
  <div class="abs brand"><span class="brand-dot"></span>R-BRIGHTLAYER</div>
  <div class="abs contact-top mail">
    <svg width="12" height="9" viewBox="0 0 12 9"><rect x=".5" y=".5" width="11" height="8" fill="none" stroke="#e8800d"/><path d="M.5 .5 6 5 11.5 .5" fill="none" stroke="#e8800d"/></svg>
    support@r-brightlayer.com</div>
  <div class="abs contact-top tel">
    <svg width="9" height="9" viewBox="0 0 10 10"><path d="M2 0 4 2.5 3 4Q4.5 6 6 7L7.5 6 10 8 8.5 10Q4 9.5 0 1.5Z" fill="#1d1d1d"/></svg>
    555-014-2260</div>
</header>

<nav class="abs nav">
  <div class="abs nav-item active" style="left:45px;width:72px">Home</div>
  <div class="abs nav-item" style="left:117px;width:70px">About us</div>
  <div class="abs nav-sep" style="left:187px"></div>
  <div class="abs nav-item" style="left:187px;width:81px">Our Mission</div>
  <div class="abs nav-sep" style="left:268px"></div>
  <div class="abs nav-item" style="left:268px;width:72px">Solutions &nbsp;▾</div>
  <div class="abs nav-sep" style="left:340px"></div>
  <div class="abs nav-item" style="left:340px;width:72px">Partners</div>
  <div class="abs nav-sep" style="left:412px"></div>
  <div class="abs nav-item" style="left:412px;width:78px">Contact us</div>
  <div class="abs search">Search..<span class="abs search-btn"></span></div>
</nav>

<section class="abs hero" role="img" aria-label="Photo of a hand inserting a card into a machine slot"></section>
<div class="abs hero-caption">
  <h2>Branch Capture</h2>
  <p>Scan and Transmit check images directly from branch to processing site</p>
</div>
<div class="abs dots"><i></i><i></i><i></i></div>
<div class="abs arrow" style="left:588px"><svg width="20" height="20"><path d="M12 6 8 10 12 14" fill="none" stroke="#fff" stroke-width="1.6"/></svg></div>
<div class="abs arrow" style="left:612px"><svg width="20" height="20"><path d="M8 6 12 10 8 14" fill="none" stroke="#fff" stroke-width="1.6"/></svg></div>

<section class="about">
  <h2 class="abs h-sec" style="left:45px;top:478px">About us</h2>
  <div class="abs rule" style="left:45px;top:511px;width:46px"></div>
  <p class="abs para" style="left:45px;top:529px;width:325px">R-Brightlayer is an Imaging Solutions company based out of Central Illinois. Being from a small town, we keep our roots in honesty and hospitality, yet our product solutionsare on the cutting edge of technology.</p>
  <p class="abs para" style="left:45px;top:583px;width:325px">We not only provide our customers valuable solutions, we do it well. We understand the needs of the institutions we serve and have the means to stay up to date on the latest advancements in the industry. From simple check archive to complex corporate</p>
  <div class="abs btn" style="left:45px;top:659px">Read More</div>
  <div class="abs about-photo" role="img" aria-label="Photo of a hand signing a check"></div>
</section>

<section class="abs solutions"></section>
<h2 class="abs h-sec" style="left:46px;top:780px">Solutions For Your Business</h2>
<div class="abs rule" style="left:46px;top:815px;width:138px"></div>
<p class="abs para" style="left:46px;top:835px;width:282px">R-Brightlayer strives to be the leading provider of cost-effective solutions to the Retail, Wholesale and Banking Marketplace. Our experience in supplying complete software, hardware, and turnkey systems enables us to provide a system that fits your needs, we don't believe in trying to change your operations to fit our products.</p>
<div class="abs btn" style="left:45px;top:926px">Read More</div>
<div class="abs sol-frame"></div>
<div class="abs sol-photo" role="img" aria-label="Photo of a desktop check scanner on a blue background"></div>

<footer class="abs footer">
  <div class="abs f-brand"><span class="brand-dot"></span>R-BRIGHTLAYER</div>
  <p class="abs f-about">Lorem Ipsum is simply dummy text of the printing and types etting industry. Lorem Ipsum</p>
  <div class="abs f-more">Read More.. &nbsp;⊙</div>

  <div class="abs f-head" style="left:202px">Quick Link</div>
  <ul class="abs f-list" style="left:202px">
    <li>Home</li><li>About us</li><li>Our Mission</li><li>Applications</li><li>Contact us</li>
  </ul>

  <div class="abs f-head" style="left:300px">Contact us</div>
  <table class="abs f-contact">
    <tr><td style="width:42px">Address :</td><td>482 Alder Grove Road<br>Maplewood, IL 60999</td></tr>
    <tr><td>Phone &nbsp;&nbsp;:</td><td>+555-014-3391</td></tr>
    <tr><td>Fax &nbsp;&nbsp;&nbsp;&nbsp;&nbsp;&nbsp;:</td><td>555-014-2260</td></tr>
    <tr><td>E-mail &nbsp;:</td><td>support@r-brightlayer.com</td></tr>
  </table>

  <div class="abs f-head" style="left:477px">Quick Contact</div>
  <div class="abs field" style="left:477px;top:70px;width:73px;height:15px">Name</div>
  <div class="abs field" style="left:558px;top:70px;width:74px;height:15px">Phone</div>
  <div class="abs field" style="left:477px;top:91px;width:155px;height:22px">Message</div>
  <div class="abs send">SEND</div>
</footer>

<div class="abs copy">Copyright 2019 R-Brightlayer, All Rights Reserved.</div>
<span class="abs social" style="left:534px"></span>
<span class="abs social" style="left:555px"></span>
<span class="abs social" style="left:577px"></span>
<span class="abs social" style="left:599px"></span>
<span class="abs social" style="left:621px"></span>

</body>
</html>
```